Regional Showdown Flyer for Holiday Program

Need a one page flyer, can be back to front or one page, ensuring you can fit all information, colourful, aimed at a market of 8-13 year old boys and girls.
The flyer needs to be noticed, needs to have certain information on it and needs to be Autralian Rule Football orientated.
Have uploaded file so you can understand the style (not content), style of flyer I am looking at getting submitted.

Target Market(s)

8-13 year old boys and girls and their parents.

Requirements
Must have
• Regional Showdown Event
• Price for Regional Showdown Day will be $85
• Strictly Limited Places, only the best footballers should enter this challenge
• Inaugural event, be the first Regional Showdown Winner for your age!
• Do you love a challenge! Put yourself to the test!
• Are you up to it - Water Slide Goal Kicking Contest! The fastest kick in the West (tested by our very own speed gun)! Can you survive the Footy Titan Trail or Last One Standing Goal Kicking! These challenges are crazy are super fun!
• If you think you can deliver on the big stage then this is for YOU!
• All District age winners will receive prizes, awards and the adulation from all their peers!
• Year's 3-5 from 9am to 12pm
• Year's 6-8 from 1-4pm
• All challengers compete against their own age
• Lunch Provided
• Monday 16th April - Upper Tarrowby Regional Showdown Day at Tarrowby Oval
• Tuesday 17th April - North Tarrowby Regional Showdown Day at Kilmorna Reserve
• Wednesday 18th April - Yarlo Regional Showdown Day - Dunhaven Football Club
• Every Challenge Participant receives a District Football!
• Need to put all 3 District Football Logos on the bottom of the flyer, logos attached at bottom.
Nice to have
• Plenty of colour, if you can fit all information on one page that would be fine
Should not have
• Dull, boring, any footballs should be Aussie Rules footballs not NFL or soccer

```html
<!DOCTYPE html>
<html lang="en">
<head>
<meta charset="utf-8">
<title>Regional Showdown Event</title>
<link rel="stylesheet" href="https://fonts.googleapis.com/css2?family=Luckiest+Guy&family=Lilita+One&family=Fredoka:wght@500;600;700&family=Oswald:wght@500;600;700&display=swap">
<style>
:root{
  --sky-top:#7fd0f2;
  --sky-bottom:#3ea7de;
  --navy:#123f8c;
  --navy-dark:#0b2d66;
  --royal:#1e5fae;
  --title-blue:#2ba4e2;
  --orange:#ff8a12;
  --red:#e4262b;
  --deep-red:#8a0f12;
  --yellow:#fff22a;
  --pink:#e8177f;
  --white:#ffffff;
  --ink:#111111;
}
*{margin:0;padding:0;box-sizing:border-box}
html,body{width:849px;height:1200px;overflow:hidden;background:var(--white)}
.flyer{position:relative;width:849px;height:1200px;overflow:hidden;
  background:radial-gradient(ellipse at 40% 30%,var(--sky-top),var(--sky-bottom) 75%);
  font-family:"Fredoka",sans-serif}
.shapes{position:absolute;inset:0}
.abs{position:absolute}

.title{font-family:"Luckiest Guy","Lilita One",sans-serif;font-weight:400;line-height:1;text-align:center;white-space:nowrap}
.title-regional{top:56px;left:130px;width:490px;font-size:84px;color:var(--title-blue);
  text-shadow:-4px -4px 0 var(--white),4px -4px 0 var(--white),-4px 4px 0 var(--white),4px 4px 0 var(--white),6px 8px 0 var(--navy)}
.title-showdown{top:146px;left:110px;width:640px;font-size:100px;color:var(--orange);
  text-shadow:-4px -4px 0 var(--white),4px -4px 0 var(--white),-4px 4px 0 var(--white),4px 4px 0 var(--white),7px 8px 0 var(--red)}
.title-event{top:256px;left:390px;width:315px;font-size:90px;color:var(--red);
  text-shadow:-4px -4px 0 var(--white),4px -4px 0 var(--white),-4px 4px 0 var(--white),4px 4px 0 var(--white),6px 7px 0 var(--deep-red)}

.football{left:70px;top:290px;width:310px;height:175px;border-radius:50%;
  transform:rotate(22deg);background:radial-gradient(ellipse at 40% 35%,#ff6a4a,#e4262b 55%,#a81414)}

.limited{left:425px;top:372px;color:var(--white)}
.limited h2{font-weight:700;font-size:26px;letter-spacing:.5px}
.limited p{font-weight:500;font-size:15px;margin-top:-4px}
.inaugural{left:480px;top:450px;color:var(--ink)}
.inaugural h2{font-weight:700;font-size:24px}
.inaugural p{font-weight:500;font-size:15px;line-height:1.05}

.challenge-call{left:86px;top:536px;font-family:"Luckiest Guy","Lilita One",sans-serif;color:var(--yellow);text-align:center;line-height:1.1;white-space:nowrap;
  text-shadow:-2px -2px 0 var(--red),2px -2px 0 var(--red),-2px 2px 0 var(--red),2px 2px 0 var(--red),4px 4px 0 var(--white)}
.challenge-call .line1{font-size:32px}
.challenge-call .line2{font-size:31px}

.price-star{left:626px;top:493px;width:250px;height:170px;background:var(--red);
  clip-path:polygon(100% 50%,84.8% 59.3%,93.3% 75%,75.5% 75.5%,75% 93.3%,59.3% 84.8%,50% 100%,40.7% 84.8%,25% 93.3%,24.5% 75.5%,6.7% 75%,15.2% 59.3%,0 50%,15.2% 40.7%,6.7% 25%,24.5% 24.5%,25% 6.7%,40.7% 15.2%,50% 0,59.3% 15.2%,75% 6.7%,75.5% 24.5%,93.3% 25%,84.8% 40.7%)}
.price-star-inner{left:651px;top:512px;width:200px;height:132px;background:var(--white);
  clip-path:polygon(100% 50%,84.8% 59.3%,93.3% 75%,75.5% 75.5%,75% 93.3%,59.3% 84.8%,50% 100%,40.7% 84.8%,25% 93.3%,24.5% 75.5%,6.7% 75%,15.2% 59.3%,0 50%,15.2% 40.7%,6.7% 25%,24.5% 24.5%,25% 6.7%,40.7% 15.2%,50% 0,59.3% 15.2%,75% 6.7%,75.5% 24.5%,93.3% 25%,84.8% 40.7%)}
.price{left:645px;top:540px;width:130px;text-align:center;font-family:"Oswald",sans-serif;color:var(--ink)}
.price .amount{font-size:50px;font-weight:700;line-height:1}
.price .only{position:absolute;left:122px;top:4px;font-size:17px;font-weight:700;transform:rotate(90deg);transform-origin:left top}
.price .lunch{font-size:15px;font-weight:600;margin-top:2px;white-space:nowrap}

.activities{left:58px;top:634px;width:310px;text-align:center;font-weight:700;color:var(--white);font-size:16px;line-height:1.08}
.activities p{margin-bottom:7px}
.activities .pink{text-shadow:-2px -2px 0 var(--pink),2px -2px 0 var(--pink),-2px 2px 0 var(--pink),2px 2px 0 var(--pink)}
.activities .navy{text-shadow:-2px -2px 0 var(--navy),2px -2px 0 var(--navy),-2px 2px 0 var(--navy),2px 2px 0 var(--navy)}
.activities .red{text-shadow:-2px -2px 0 var(--red),2px -2px 0 var(--red),-2px 2px 0 var(--red),2px 2px 0 var(--red)}
.activities small{font-size:13px}

.big-stage{left:400px;top:668px;width:420px;text-align:center;color:var(--white);font-family:"Oswald",sans-serif}
.big-stage .lead{font-size:20px;font-weight:500;transform:rotate(-2deg)}
.big-stage .for-you{font-family:"Fredoka",sans-serif;font-size:36px;font-weight:700;margin-top:-2px;transform:rotate(-2deg)}
.sessions{left:420px;top:748px;width:420px;text-align:center;color:var(--white);font-family:"Fredoka",sans-serif;font-weight:700;font-size:19px;line-height:1.08}
.own-age{left:400px;top:805px;width:380px;text-align:center;font-family:"Oswald",sans-serif;font-weight:500;font-size:19px;line-height:28px;color:var(--ink);white-space:nowrap}

.dates{left:150px;top:856px;width:640px;text-align:center;color:var(--white);font-family:"Oswald",sans-serif}
.dates .day{font-size:20px;font-weight:700;line-height:1.1}
.dates .day sup{font-size:11px}
.dates .place{font-size:16px;font-weight:600;line-height:1.1;margin-bottom:13px}

.giveaway{left:150px;top:1027px;font-weight:600;font-size:21px;color:var(--ink)}

.partners{left:0;top:1063px;width:849px;height:120px;display:flex;justify-content:space-around;align-items:center;padding:0 70px}
.partner{display:flex;align-items:center;gap:10px;font-weight:700;font-size:20px;color:var(--navy);font-family:"Fredoka",sans-serif}
.partner .dot{width:38px;height:38px;border-radius:50%;background:var(--navy)}
</style>
</head>
<body>
<main class="flyer">
  <svg class="shapes" width="849" height="1200" viewBox="0 0 849 1200" aria-hidden="true">
    <polygon points="392,362 849,354 849,424 400,431" fill="var(--royal)"/>
    <polygon points="470,441 849,446 849,517 478,520" fill="var(--yellow)"/>
    <polygon points="300,662 849,640 849,849 380,849" fill="var(--royal)"/>
    <polygon points="403,740 849,732 849,797 410,801" fill="var(--red)"/>
    <polygon points="390,800 790,797 772,840 400,842" fill="var(--yellow)"/>
    <polygon points="135,849 806,849 806,1016 107,1016" fill="var(--navy)"/>
    <polygon points="790,860 806,849 806,1016 790,1000" fill="var(--navy-dark)"/>
    <polygon points="0,1016 784,1016 770,1067 0,1067" fill="var(--yellow)"/>
    <rect x="0" y="1063" width="849" height="120" fill="var(--white)"/>
    <rect x="0" y="1183" width="849" height="17" fill="var(--title-blue)"/>
  </svg>

  <h1>
    <span class="abs title title-regional">REGIONAL</span>
    <span class="abs title title-showdown">SHOWDOWN</span>
    <span class="abs title title-event">EVENT</span>
  </h1>

  <div class="abs football" role="img" aria-label="Red Australian Rules football"></div>

  <div class="abs limited">
    <h2>STRICTLY LIMITED PLACES</h2>
    <p>only the best footballers should enter this challenge</p>
  </div>

  <div class="abs inaugural">
    <h2>INAUGURAL EVENT</h2>
    <p>be the first Regional Showdown Winner<br>for your age!</p>
  </div>

  <div class="abs challenge-call">
    <div class="line1">DO YOU LOVE A CHALLENGE!</div>
    <div class="line2">PUT YOURSELF TO THE TEST!</div>
  </div>

  <div class="abs price-star"></div>
  <div class="abs price-star-inner"></div>
  <div class="abs price">
    <div class="amount">$85</div>
    <span class="only">ONLY</span>
    <div class="lunch">(LUNCH PROVIDED)</div>
  </div>

  <div class="abs activities">
    <p class="pink">Are you up to it<br>Water Slide Goal Kicking Contest!<br>The fastest kick in the West<br><small>(tested by our very own speed gun)!</small></p>
    <p class="navy">Can you survive the Footy Titan Trail or Last One Standing Goal Kicking! These challenges are crazy are super fun!</p>
    <p class="red">All District age winners will receive prizes, awards and the adulation from all their peers!</p>
  </div>

  <div class="abs big-stage">
    <div class="lead">If you think you can deliver on the big stage then</div>
    <div class="for-you">This is for YOU!</div>
  </div>

  <div class="abs sessions">YEAR'S 3-5 FROM 9AM TO 12PM<br>YEAR'S 6-8 FROM 1-4PM</div>
  <div class="abs own-age">All challengers compete against their own age</div>

  <div class="abs dates">
    <div class="day">MONDAY 16<sup>TH</sup> APRIL</div>
    <div class="place">UPPER TARROWBY REGIONAL SHOWDOWN DAY AT TARROWBY OVAL</div>
    <div class="day">TUESDAY 17<sup>TH</sup> APRIL</div>
    <div class="place">NORTH TARROWBY REGIONAL SHOWDOWN DAY AT KILMORNA RESERVE</div>
    <div class="day">WEDNESDAY 18<sup>TH</sup> APRIL</div>
    <div class="place">YARLO REGIONAL SHOWDOWN DAY - DUNHAVEN FOOTBALL CLUB</div>
  </div>

  <div class="abs giveaway">Every Challenge Participant receives a District Football!</div>

  <footer class="abs partners">
    <div class="partner"><span class="dot"></span>Ironbarks District</div>
    <div class="partner"><span class="dot"></span>Stingrays District</div>
    <div class="partner"><span class="dot"></span>Yarlo District</div>
  </footer>
</main>
</body>
</html>
```